Dental Practice based in Melbourne needs header designed for mobile website

Evergrove Dental Carlton needs logo modified (better color scheme)and the header needs good use of colors (Green should be one of them) . The overall scheme is attached below. Please maintain the overall position of the logo in the center just like the way it is. Icons that should be present : Evergrove Dental Carlton, Phone number with phone icon, Menu bar, Book now, search icon, Logo. in the center.

```html
<!DOCTYPE html>
<html lang="en">
<head>
<meta charset="utf-8">
<title>Evergrove Dental Carlton – Mobile Header</title>
<link rel="stylesheet" href="https://fonts.googleapis.com/css2?family=Poppins:wght@500;600;700&display=swap">
<style>
  :root {
    --charcoal: #3a383d;
    --logo-light: #eef0f4;
    --green: #20c06f;
    --green-deep: #1aa961;
    --white: #ffffff;
    --photo-light: #ece8e2;
    --photo-mid: #d9cbb8;
    --photo-warm: #c98b3f;
  }
  * { margin: 0; padding: 0; box-sizing: border-box; }
  html, body { width: 675px; height: 1200px; overflow: hidden; background: var(--white); }
  body { font-family: "Poppins", sans-serif; }

  .site-header { width: 675px; }

  .brand-bar {
    height: 90px;
    background: var(--charcoal);
    display: flex;
    align-items: center;
    justify-content: space-between;
    padding: 0 27px;
  }
  .brand {
    display: flex;
    align-items: center;
    gap: 12px;
  }
  .brand-mark {
    width: 30px;
    height: 30px;
    border-radius: 50%;
    background: var(--green);
    flex: none;
  }
  .brand-name {
    color: var(--logo-light);
    font-weight: 700;
    font-size: 19px;
    line-height: 1;
    letter-spacing: 0.6px;
    text-transform: uppercase;
    white-space: nowrap;
  }
  .menu-toggle { display: block; width: 33px; height: 27px; }

  .action-bar {
    height: 43px;
    background: var(--green);
    display: flex;
    align-items: center;
    color: var(--white);
  }
  .search-button {
    width: 43px; height: 43px;
    display: flex; align-items: center; justify-content: center;
  }
  .book-button {
    height: 43px;
    width: 108px;
    background: var(--green-deep);
    display: flex; align-items: center; justify-content: center;
    font-weight: 600; font-size: 13.5px;
    letter-spacing: 0.2px;
    white-space: nowrap;
  }
  .phone-link {
    margin-left: auto;
    margin-right: 27px;
    display: flex; align-items: center; gap: 9px;
    font-weight: 600; font-size: 15.5px;
    white-space: nowrap;
  }

  .hero-photo {
    height: 315px;
    background: linear-gradient(100deg, var(--photo-light) 0%, var(--photo-mid) 30%, var(--photo-warm) 55%, var(--photo-mid) 72%, var(--photo-light) 100%);
  }
</style>
</head>
<body>
  <header class="site-header">
    <div class="brand-bar">
      <div class="brand">
        <span class="brand-mark" aria-hidden="true"></span>
        <span class="brand-name">Evergrove Dental Carlton</span>
      </div>
      <svg class="menu-toggle" viewBox="0 0 33 27" aria-label="Menu">
        <rect x="0" y="0" width="33" height="3" fill="var(--white)"/>
        <rect x="0" y="12" width="33" height="3" fill="var(--white)"/>
        <rect x="0" y="24" width="33" height="3" fill="var(--white)"/>
      </svg>
    </div>
    <div class="action-bar">
      <span class="search-button" aria-label="Search">
        <svg width="19" height="19" viewBox="0 0 19 19">
          <circle cx="8" cy="8" r="5.8" fill="none" stroke="var(--white)" stroke-width="2.8"/>
          <line x1="12.3" y1="12.3" x2="17" y2="17" stroke="var(--white)" stroke-width="3.2" stroke-linecap="round"/>
        </svg>
      </span>
      <span class="book-button">BOOK NOW</span>
      <span class="phone-link">
        <svg width="19" height="19" viewBox="0 0 24 24" aria-hidden="true">
          <path fill="var(--white)" d="M6.6 10.8a15.1 15.1 0 0 0 6.6 6.6l2.2-2.2c.3-.3.7-.4 1-.2 1.1.4 2.3.6 3.6.6.6 0 1 .4 1 1V20c0 .6-.4 1-1 1A17 17 0 0 1 3 4c0-.6.4-1 1-1h3.5c.6 0 1 .4 1 1 0 1.3.2 2.5.6 3.6.1.3 0 .7-.2 1z"/>
        </svg>
        (03) 94125530
      </span>
    </div>
    <div class="hero-photo" role="img" aria-label="Photo of a smiling woman looking at her reflection in a white framed mirror"></div>
  </header>
</body>
</html>
```